Business Card Design

I need a business card design for a new company based in Sydney called 'The Copper Ladle'. We deliver organic, gourmet and fine foods to your door.

I would like to see creative, unique designs which use colours which represent health and nature like green.

Target Market(s)

Health conscious 20 to 35 year olds.

Industry/Entity Type

Health

Contact Information for Business Card

The Copper Ladle, Owen Barclett, owen@thecopperladle.com.au, 0427685392

Requirements
Must have
• My logo.

```html
<!DOCTYPE html>
<html lang="en">
<head>
<meta charset="utf-8">
<title>The Copper Ladle – Business Card</title>
<link href="https://fonts.googleapis.com/css2?family=Open+Sans:wght@400;600;700&display=swap" rel="stylesheet">
<style>
  :root {
    --page: #e6e7e8;
    --card: #f7f7f7;
    --green: #3f9a2c;
    --green-light: #8cc63f;
    --line-soft: #b6dca0;
    --ink: #2f2f2f;
    --slate: #4a5a6a;
    --white: #ffffff;
  }
  * { box-sizing: border-box; margin: 0; padding: 0; }
  html, body {
    width: 1200px; height: 1026px; overflow: hidden;
    background: var(--page);
    font-family: "Open Sans", Arial, sans-serif;
    color: var(--ink);
  }
  .canvas {
    position: relative; width: 1200px; height: 1026px;
    display: flex; flex-direction: column; align-items: center; justify-content: center; gap: 56px;
  }
  .card {
    position: relative; width: 840px; height: 460px;
    background: var(--card);
    box-shadow: 0 2px 10px rgba(0,0,0,0.12);
    overflow: hidden;
  }

  /* Brand lockup */
  .brand { display: flex; align-items: center; gap: 14px; }
  .brand-dot { width: 46px; height: 46px; border-radius: 50%; background: var(--green-light); flex: none; }
  .brand-name { font-weight: 600; color: var(--green); line-height: 1; white-space: nowrap; }

  /* Logo side */
  .card-logo { display: flex; flex-direction: column; align-items: center; justify-content: center; }
  .card-logo .brand-name { font-size: 40px; }
  .card-logo .website { margin-top: 46px; font-size: 19px; color: var(--ink); }

  /* Contact side */
  .name-band { position: absolute; left: 0; top: 0; width: 840px; height: 110px; }
  .person-name {
    position: absolute; left: 30px; top: 54px;
    font-size: 27px; font-weight: 700; letter-spacing: 0.5px; line-height: 1.2;
    color: var(--white); text-transform: uppercase;
  }
  .person-role {
    position: absolute; left: 424px; top: 58px;
    font-size: 20px; font-weight: 700; line-height: 1.2; color: var(--slate);
  }
  .contact-item { position: absolute; left: 26px; display: flex; align-items: flex-start; }
  .item-address { top: 128px; }
  .item-phone { top: 198px; }
  .item-email { top: 294px; }
  .item-web { top: 364px; }
  .contact-icon {
    width: 46px; flex: none; display: flex; flex-direction: column; align-items: flex-start;
  }
  .contact-icon svg { width: 26px; height: 26px; }
  .contact-icon::after {
    content: ""; display: block; width: 40px; height: 2px; margin-top: 10px; background: var(--line-soft);
  }
  .contact-text { padding-left: 22px; font-size: 19px; line-height: 1.3; color: var(--ink); white-space: nowrap; }
  .accent-band { position: absolute; left: 0; top: 260px; width: 840px; height: 20px; }
  .card-contact .brand { position: absolute; right: 40px; bottom: 44px; }
  .card-contact .brand-name { font-size: 38px; }
  .card-contact .brand-dot { width: 52px; height: 52px; }
</style>
</head>
<body>
<main class="canvas">

  <section class="card card-logo" aria-label="Business card, logo side">
    <div class="brand">
      <span class="brand-dot"></span>
      <span class="brand-name">The Copper Ladle</span>
    </div>
    <p class="website">www.thecopperladle.com.au</p>
  </section>

  <section class="card card-contact" aria-label="Business card, contact side">
    <svg class="name-band" viewBox="0 0 840 110" aria-hidden="true">
      <path d="M0 40 H366 C386 40 386 92 412 92 H840 V100 H0 Z" fill="var(--green)"/>
    </svg>
    <h1 class="person-name">Owen Barclett</h1>
    <p class="person-role">Managing Director</p>

    <svg class="accent-band" viewBox="0 0 840 20" aria-hidden="true">
      <rect x="0" y="9" width="330" height="2" fill="var(--line-soft)"/>
      <path d="M330 3 H840 V17 H320 Z" fill="var(--green)"/>
    </svg>

    <div class="contact-item item-address">
      <span class="contact-icon">
        <svg viewBox="0 0 24 24"><path d="M12 2a7 7 0 0 0-7 7c0 5 7 13 7 13s7-8 7-13a7 7 0 0 0-7-7zm0 9.5A2.5 2.5 0 1 1 12 6.5a2.5 2.5 0 0 1 0 5z" fill="var(--green)"/></svg>
      </span>
      <span class="contact-text">Level 3, 27 Harbour Lane<br>Surry Hills NSW</span>
    </div>
    <div class="contact-item item-phone">
      <span class="contact-icon">
        <svg viewBox="0 0 24 24"><path d="M6.6 10.8a15.1 15.1 0 0 0 6.6 6.6l2.2-2.2a1 1 0 0 1 1-.25 11.4 11.4 0 0 0 3.6.57 1 1 0 0 1 1 1V20a1 1 0 0 1-1 1A17 17 0 0 1 3 4a1 1 0 0 1 1-1h3.5a1 1 0 0 1 1 1c0 1.25.2 2.45.57 3.57a1 1 0 0 1-.25 1z" fill="var(--green)"/></svg>
      </span>
      <span class="contact-text">0427 685 392<br>02 9184 7730</span>
    </div>
    <div class="contact-item item-email">
      <span class="contact-icon">
        <svg viewBox="0 0 24 24"><rect x="2" y="5" width="20" height="14" rx="1.5" fill="var(--green)"/><path d="M3 6.5l9 6.5 9-6.5" fill="none" stroke="var(--white)" stroke-width="1.6"/></svg>
      </span>
      <span class="contact-text">owen@thecopperladle.com.au</span>
    </div>
    <div class="contact-item item-web">
      <span class="contact-icon">
        <svg viewBox="0 0 24 24"><g fill="none" stroke="var(--green)" stroke-width="1.8"><circle cx="12" cy="12" r="9.5"/><ellipse cx="12" cy="12" rx="4.2" ry="9.5"/><path d="M2.5 12h19M4 7h16M4 17h16"/></g></svg>
      </span>
      <span class="contact-text">www.thecopperladle.com.au</span>
    </div>

    <div class="brand">
      <span class="brand-dot"></span>
      <span class="brand-name">The Copper Ladle</span>
    </div>
  </section>

</main>
</body>
</html>
```